Flyer-Design für ein kleines Familienunternehmen
Zielgruppe
Wir sind ein kleines Familienunternehmen, welche gewerbliche Kaffeemaschinen verkauft und den service darum anbietet.
Unsere Homepage: https://www.morgenbohne-handel.de/
Wir möchten eine neue Zielgruppe erschließen.
Die neue Zielgruppe sind Büros.
Angebot ist : - Service
- Kaffee Lieferung
- Rund um Paket
Aufgabenstellung
Merkmal der Familienunternehmen und Regionalität soll deutlich werden.
Wir Bieten: schnelle; einfache; individuelle Lösung
Rund um Sorglos.

```html
<!DOCTYPE html>
<html lang="de">
<head>
<meta charset="utf-8">
<title>Morgenbohne – Flyer Vorder- und Rückseite</title>
<link rel="stylesheet" href="https://fonts.googleapis.com/css2?family=Bebas+Neue&family=Raleway:wght@400;500;600&display=swap">
<style>
  :root {
    --bg: #d6c697;
    --tan: #a89383;
    --mint: #b9dcb9;
    --white: #ffffff;
    --brown: #4b2a12;
    --photo-warm: #8a7a68;
    --photo-light: #d9d4cc;
    --photo-dark: #3c3f44;
    --shadow: rgba(60, 45, 20, 0.25);
  }
  * { box-sizing: border-box; margin: 0; padding: 0; }
  html, body { width: 1111px; height: 1200px; overflow: hidden; }
  body {
    background: var(--bg);
    font-family: "Raleway", sans-serif;
    position: relative;
  }
  .flyer {
    position: absolute;
    left: 56px;
    width: 1000px;
    height: 460px;
    display: grid;
    grid-template-columns: repeat(4, 250px);
    grid-template-rows: repeat(2, 230px);
    box-shadow: 0 24px 40px var(--shadow);
    background: var(--white);
    overflow: hidden;
  }
  .flyer--front { top: 90px; }
  .flyer--back { top: 650px; }

  .cell { position: relative; overflow: hidden; }
  .cell--tan { background: var(--tan); color: var(--white); }
  .cell--mint { background: var(--mint); color: var(--white); }
  .cell--white { background: var(--white); }

  .photo {
    width: 100%; height: 100%;
    background: linear-gradient(160deg, var(--photo-light) 0%, var(--photo-warm) 55%, var(--photo-dark) 100%);
  }
  .photo--wide {
    background: linear-gradient(180deg, var(--photo-light) 0%, #b3aaa0 45%, var(--photo-dark) 100%);
  }
  .photo-caption {
    position: absolute; right: 12px; bottom: 10px;
    color: var(--white); font-size: 12px; font-weight: 500;
  }

  .headline {
    font-family: "Bebas Neue", sans-serif;
    line-height: 0.88;
    color: var(--white);
    letter-spacing: 0.5px;
    font-weight: 400;
  }
  .headline--xl { font-size: 104px; }
  .headline--lg { font-size: 76px; }
  .headline--md { font-size: 36px; }
  .headline--sm { font-size: 30px; }
  .headline--name { font-size: 44px; }

  .brand {
    display: flex; flex-direction: column; align-items: center; justify-content: center;
    height: 100%; text-align: center; color: var(--brown); padding: 0 12px;
  }
  .brand__mark { display: flex; align-items: center; gap: 8px; }
  .brand__dot { width: 14px; height: 14px; border-radius: 50%; background: var(--brown); flex: none; }
  .brand__name { font-size: 27px; font-weight: 600; }
  .brand__tagline { font-size: 11px; margin-top: 8px; line-height: 1.3; }
  .brand__url { font-size: 13px; margin-top: 26px; font-weight: 500; }

  .front-word { display: flex; align-items: center; justify-content: center; height: 100%; }
  .front-word--bottom { align-items: flex-end; padding-bottom: 16px; }

  .copy { font-size: 11.5px; line-height: 1.3; color: var(--white); }
  .copy--small { font-size: 11px; }
  .pad { padding: 18px 20px; }

  .intro { display: flex; flex-direction: column; justify-content: space-between; height: 100%; }

  .machine-thumb {
    position: absolute; top: 14px; right: 16px; width: 56px; height: 38px;
    background: linear-gradient(180deg, #eeeeee, #9a9a9a);
  }
  .sub { font-size: 12px; margin-top: 12px; color: var(--white); }

  .deliver { display: flex; gap: 12px; }
  .badges { display: flex; flex-direction: column; gap: 8px; flex: none; }
  .badge { width: 26px; height: 26px; background: var(--white); }

  .contact .copy + .copy { margin-top: 10px; }
  .contact .headline { margin-top: 10px; }
  .contact .legal { font-size: 11px; color: var(--white); margin-top: 4px; line-height: 1.3; }
</style>
</head>
<body>

  <section class="flyer flyer--front" aria-label="Flyer Vorderseite">
    <div class="cell cell--white">
      <div class="brand">
        <div class="brand__mark"><span class="brand__dot"></span><span class="brand__name">Morgenbohne</span></div>
        <p class="brand__tagline">Espresso im Büro<br>wie beim Italiener</p>
        <p class="brand__url">morgenbohne-handel.de</p>
      </div>
    </div>
    <div class="cell">
      <div class="photo" role="img" aria-label="Porträt von B. Brandhorst in der Werkstatt"></div>
      <span class="photo-caption">B. Brandhorst</span>
    </div>
    <div class="cell cell--tan">
      <div class="front-word"><span class="headline headline--lg">Kaffee</span></div>
    </div>
    <div class="cell">
      <div class="photo" role="img" aria-label="Porträt von D. Brandhorst vor gefliester Wand"></div>
      <span class="photo-caption">D. Brandhorst</span>
    </div>
    <div class="cell">
      <div class="photo" role="img" aria-label="Porträt von A. Brandhorst in der Werkstatt"></div>
      <span class="photo-caption">A. Brandhorst</span>
    </div>
    <div class="cell cell--tan">
      <div class="front-word"><span class="headline headline--xl">Büro</span></div>
    </div>
    <div class="cell">
      <div class="photo" role="img" aria-label="Porträt von C. Brandhorst vor einem Regal"></div>
      <span class="photo-caption">C. Brandhorst</span>
    </div>
    <div class="cell cell--mint">
      <div class="front-word front-word--bottom"><span class="headline headline--name">Brandhorst</span></div>
    </div>
  </section>

  <section class="flyer flyer--back" aria-label="Flyer Rückseite">
    <div class="cell cell--mint pad">
      <div class="machine-thumb" role="img" aria-label="Kleines Foto einer Siebträgermaschine"></div>
      <h2 class="headline headline--md">Den<br>leckersten<br>Kaffee<br>im Büro</h2>
      <p class="sub">Den machst jetzt DU!</p>
    </div>
    <div class="cell cell--tan pad">
      <div class="intro">
        <p class="copy copy--small">WIR sind Dir bei der Auswahl Deiner Maschine behilflich und auch danach immer Dein Ansprechpartner.<br>Wir bieten einfache Lösungen für Deinen Kaffee im Büro: Individuelle Beratung – Gute Maschinen – Leckeren Kaffee – perfekten Service.</p>
        <h2 class="headline headline--sm">Bei uns bist<br>du richtig</h2>
      </div>
    </div>
    <div class="cell" style="grid-column: span 2;">
      <div class="photo photo--wide" role="img" aria-label="Die vier Familienmitglieder hinter einer Siebträgermaschine"></div>
    </div>
    <div class="cell cell--tan pad">
      <div class="deliver">
        <div class="badges" aria-label="Partnermarken">
          <span class="badge"></span><span class="badge"></span><span class="badge"></span><span class="badge"></span><span class="badge"></span>
        </div>
        <div>
          <h2 class="headline headline--md">Wir<br>liefern</h2>
          <p class="copy" style="margin-top:4px">ausgewählten Kaffee:<br>Ob Wiener Kaffeehaus Kultur, Bio FAIR-TRADE Kaffee oder den vielleicht nachhaltigsten Kaffee der Welt</p>
        </div>
      </div>
    </div>
    <div class="cell cell--white">
      <div class="brand">
        <div class="brand__mark"><span class="brand__dot"></span><span class="brand__name">Morgenbohne</span></div>
        <p class="brand__tagline">Espresso im Büro<br>wie beim Italiener</p>
        <p class="brand__url">morgenbohne-handel.de</p>
      </div>
    </div>
    <div class="cell cell--mint pad">
      <h2 class="headline headline--md">Rundum<br>sorglos</h2>
      <p class="copy" style="margin-top:8px">Wir stehen an Deiner Seite – mit schnellen, einfachen individuellen Lösungen – bei Finanzierung, Kauf oder Miete und technischem Support.</p>
    </div>
    <div class="cell cell--tan pad contact">
      <p class="copy">Und wenn's mal klemmt?<br>Unser Technik-Sorglos-Paket: Du rufst an und wir helfen Dir schon am Telefon.</p>
      <p class="copy">0 22 37 / 55 018 20<br>office@morgenbohne-kaffee.de</p>
      <h2 class="headline headline--name">Brandhorst</h2>
      <p class="legal">Brandhorst Kaffeemaschinen e.K.<br>Lindenweg 12, 50171 Feldkirchen</p>
    </div>
  </section>

</body>
</html>
```